QDN Business Cards

I would like to use deep red (See attached logo), medium grays and white on the card to be used as separators for information using a white font over the red and gray colors. We are a web application design and development firm - specializing in custom software development with a content management solution. Our card needs to reflect innovative and cutting edge company.
I have attached the current card for content purposes - there is a front and back to the card. Open to suggestions on layout.

```html
<!DOCTYPE html>
<html lang="en">
<head>
<meta charset="utf-8">
<title>QDN Tech Group – Business Cards</title>
<link rel="stylesheet" href="https://fonts.googleapis.com/css2?family=Lato:ital,wght@0,400;0,700;0,900;1,700&display=swap">
<style>
  :root {
    --red: #c8282f;
    --red-deep: #b3222a;
    --blush: #f4e4e2;
    --charcoal: #2b2b2b;
    --gray: #6f6f6f;
    --gray-light: #d9d9d9;
    --white: #ffffff;
    --stage: #e9e9e9;
  }
  * { box-sizing: border-box; margin: 0; padding: 0; }
  html, body { width: 1200px; height: 900px; overflow: hidden; }
  body {
    background: var(--stage);
    font-family: "Lato", sans-serif;
    position: relative;
  }
  .card {
    position: absolute;
    width: 540px;
    height: 330px;
    top: 285px;
    box-shadow: 0 10px 22px rgba(0,0,0,.25);
    overflow: hidden;
  }

  /* ---------- Shared brand line ---------- */
  .brand {
    position: absolute; left: 0; right: 0;
    display: flex; align-items: center; justify-content: center; gap: 10px;
    color: var(--charcoal); font-weight: 900; white-space: nowrap; line-height: 1;
  }
  .brand-dot { flex: none; border-radius: 50%; background: var(--red); }

  /* ---------- Front ---------- */
  .card-front {
    left: 40px;
    background: linear-gradient(to bottom, var(--blush) 0%, #e9c3bf 35%, #d65a58 62%, var(--red) 85%, var(--red-deep) 100%);
  }
  .tagline {
    position: absolute; top: 18px; left: 0; width: 100%;
    text-align: center; color: var(--red);
    font-weight: 900; font-size: 17px; letter-spacing: .2px;
  }
  .tagline-rule {
    position: absolute; top: 42px; left: 45px; right: 35px;
    height: 1px; background: var(--charcoal);
  }
  .card-front .brand { top: 84px; font-size: 32px; }
  .card-front .brand-dot { width: 16px; height: 16px; }

  .name-bar {
    position: absolute; top: 150px; left: 45px; right: 25px; height: 40px;
    display: flex;
  }
  .greeting {
    width: 95px; background: var(--white); border: 2px solid var(--gray-light);
    display: flex; align-items: center; justify-content: center;
    font-style: italic; font-weight: 700; font-size: 13px; color: var(--charcoal);
    position: relative; z-index: 1;
  }
  .greeting::after {
    content: ""; position: absolute; right: -11px; top: 50%; transform: translateY(-50%);
    border-left: 10px solid var(--white); border-top: 9px solid transparent; border-bottom: 9px solid transparent;
  }
  .full-name {
    flex: 1; background: var(--charcoal); color: var(--white);
    display: flex; align-items: center; justify-content: center;
    font-size: 19px; font-weight: 400; letter-spacing: .3px; white-space: nowrap;
  }
  .full-name strong { font-weight: 900; margin-right: 6px; }
  .role {
    width: 120px; background: var(--white); color: #9a9a9a;
    display: flex; align-items: center; justify-content: center;
    font-size: 10px; font-weight: 700;
  }
  .contact-row {
    position: absolute; top: 198px; left: 45px; right: 25px; height: 108px;
    display: flex; gap: 6px;
  }
  .contact-box {
    flex: 1; background: var(--red);
    color: var(--white); font-size: 10.5px; line-height: 1.35;
    display: flex; flex-direction: column; align-items: center; padding-top: 14px;
    text-align: center; white-space: nowrap;
  }
  .contact-box svg { width: 16px; height: 16px; margin-bottom: 14px; fill: var(--white); }
  .contact-box .phones { text-align: left; }

  /* ---------- Back ---------- */
  .card-back { left: 620px; background: var(--red); }
  .back-frame {
    position: absolute; inset: 30px 28px; background: var(--gray-light); padding: 8px;
  }
  .back-panel { width: 100%; height: 100%; background: var(--white); position: relative; }
  .card-back .brand { top: 30px; font-size: 30px; }
  .card-back .brand-dot { width: 15px; height: 15px; }
  .services {
    position: absolute; top: 86px; left: 0; width: 100%;
    text-align: center; color: var(--gray); font-weight: 900;
    font-size: 13.5px; line-height: 1.28; letter-spacing: .3px; white-space: nowrap;
  }
  .services-rule {
    position: absolute; top: 160px; left: 10px; right: 10px; height: 1px; background: var(--gray);
  }
  .follow {
    position: absolute; top: 172px; width: 100%; text-align: center;
    color: var(--red); font-weight: 900; font-size: 13px;
  }
  .social {
    position: absolute; top: 196px; left: 0; right: 0;
    display: flex; justify-content: center; gap: 14px;
  }
  .social span { width: 22px; height: 22px; background: #3b67a8; border-radius: 3px; }
  .social span.wide { width: 60px; background: var(--red); }
</style>
</head>
<body>

<section class="card card-front" aria-label="Business card front">
  <p class="tagline">WOMAN OWNED SMALL BUSINESS</p>
  <div class="tagline-rule"></div>

  <div class="brand"><span class="brand-dot"></span>QDN Tech Group</div>

  <div class="name-bar">
    <div class="greeting">HELLO, I'M</div>
    <div class="full-name"><strong>DANA</strong> WHITFIELD</div>
    <div class="role">PRESIDENT</div>
  </div>

  <div class="contact-row">
    <div class="contact-box">
      <svg viewBox="0 0 16 16" aria-hidden="true"><path d="M8 1 0 8h2v7h4v-5h4v5h4V8h2z"/></svg>
      <span>2200 Harbor Lane Suite 300<br>Fairview, MD 20900</span>
    </div>
    <div class="contact-box">
      <svg viewBox="0 0 16 16" aria-hidden="true"><path d="M2 4c2-2 10-2 12 0l-1 3h-3V5H6v2H3zM3 8h10l1 6H2zm5 1.5a2 2 0 1 0 0 4 2 2 0 0 0 0-4z"/></svg>
      <span class="phones">O:&nbsp; 240 - 555 - 0142<br>F:&nbsp; 240 - 555 - 0187<br>C:&nbsp; 703 - 555 - 0119</span>
    </div>
    <div class="contact-box">
      <svg viewBox="0 0 16 16" aria-hidden="true"><path d="M1 2h14v9H1zm2 2v5h10V4zM6 12h4v1h2v1H4v-1h2z"/></svg>
      <span>dana@qdntechgroup.com<br>www.qdntechgroup.com</span>
    </div>
  </div>
</section>

<section class="card card-back" aria-label="Business card back">
  <div class="back-frame">
    <div class="back-panel">
      <div class="brand"><span class="brand-dot"></span>QDN Tech Group</div>
      <p class="services">
        PROJECT MGMT/STRATEGY / WEB APP DEVELOPMENT<br>
        MOBILE APP / DESIGN / SECTION 508 / TRAINING<br>
        STAFFING / SOCIAL MEDIA / ADVERTISTING / MARKETING
      </p>
      <div class="services-rule"></div>
      <p class="follow">Follow us: @ QDNTECHGROUP</p>
      <div class="social" aria-label="Social channels">
        <span></span><span></span><span></span><span class="wide"></span>
      </div>
    </div>
  </div>
</section>

</body>
</html>
```